Harbor Oncology Partners Patient Referral Card

We need a 3.75" wide by 8.25" long patient referral card that a physician will fill out to refer their patient to Harbor Oncology Partners. The front of the card will have our logo on top, followed by contact information, a map that shows the office location and then there will be descriptive text at the bottom. On the back side, there will be a headshot photo with a brief bio of Dr. Marcus Whitfield. The address for the office is: 4175 N. Larchmont, Puyallup, WA 98461. The office phone number is 253.400.7218 and the website address is: harboroncologyhub.com

Target Market(s)

Physicians and medical staff

Font styles to use
Serif

Colors
34a7d8
33b8a4
9bcb3c

Requirements
Must have
• A map of the office location and two text boxes for descriptive language about services, and a photo and bio of Dr. Marcus Whitfield
Nice to have
• Clean and distinct design that is eye catching
Should not have
• Flowery or bold colors that distract from the content and purpose of the card

```html
<!DOCTYPE html>
<html lang="en">
<head>
<meta charset="utf-8">
<title>Harbor Oncology Partners – Referral Card</title>
<link href="https://fonts.googleapis.com/css2?family=Nunito+Sans:wght@400;600;700&display=swap" rel="stylesheet">
<style>
:root{
  --blue:#34a7d8;
  --teal:#33b8a4;
  --green:#9bcb3c;
  --panel-top:#5bbb48;
  --panel-bottom:#46c3cd;
  --ink:#3d3d3d;
  --ink-soft:#555;
  --stage:#eceded;
  --map:#616161;
}
*{box-sizing:border-box;margin:0;padding:0}
html,body{width:1200px;height:1200px;overflow:hidden}
body{background:radial-gradient(circle at 50% 50%,#fafafa 0%,var(--stage) 75%);font-family:"Nunito Sans",sans-serif;position:relative}
.card{position:absolute;top:362px;width:217px;height:475px;background:#fff;overflow:hidden}
.card--front{left:358px}
.card--back{left:626px}

/* front */
.accent-bar{position:absolute;top:0;left:0;right:0;height:4px;background:linear-gradient(90deg,var(--blue) 0 69%,var(--green) 69% 100%)}
.brand{position:absolute;top:30px;left:0;right:0;display:flex;align-items:center;justify-content:center;gap:6px}
.brand__dot{width:14px;height:14px;border-radius:50%;background:var(--teal);flex:none}
.brand__name{font-size:14px;line-height:1.15;font-weight:600;color:var(--teal);letter-spacing:.5px;width:120px}
.contact{position:absolute;top:96px;left:0;right:0;text-align:center}
.contact__label{font-size:9px;color:var(--ink);letter-spacing:.2px}
.contact__phone{font-size:19px;font-weight:700;color:var(--teal);line-height:1.1}
.offer{position:absolute;top:148px;left:11px;right:10px;color:var(--ink-soft)}
.offer__title{font-size:11px;font-weight:600;color:var(--ink);margin-bottom:7px}
.offer p{font-size:10.4px;line-height:16.8px;margin-bottom:7px}
.map{position:absolute;top:311px;left:0;right:0;height:145px;background:linear-gradient(160deg,#6a6a6a,var(--map))}
.footer-band{position:absolute;bottom:0;left:0;right:0;height:19px;background:var(--blue)}

/* back */
.profile{position:absolute;top:0;left:0;right:0;height:376px;background:linear-gradient(180deg,var(--panel-top),var(--panel-bottom));color:#fff}
.profile__photo{position:absolute;top:14px;left:66px;width:85px;height:85px;border-radius:50%;border:3px solid #fff;background:radial-gradient(circle at 50% 40%,#c9b3a5,#4a4a52 70%)}
.profile__name{position:absolute;top:101px;left:0;right:0;text-align:center;font-size:11px;font-weight:700;letter-spacing:.2px}
.profile__role{position:absolute;top:115px;left:0;right:0;text-align:center;font-size:7.6px}
.about{position:absolute;top:140px;left:11px;right:9px}
.about__title{font-size:11px;font-weight:600;margin-bottom:5px}
.about p{font-size:9.2px;line-height:12.8px;margin-bottom:12.8px}
.office{position:absolute;top:386px;left:0;right:0;text-align:center;color:var(--ink)}
.office__title{font-size:11px}
.office__address{font-size:8.6px;margin-top:3px;display:flex;align-items:center;justify-content:center;gap:2px}
.office__rule{position:absolute;top:427px;left:8px;right:8px;height:1px;background:#e3e3e3}
.links{position:absolute;top:442px;left:0;right:0;display:flex;justify-content:space-around;padding:0 4px;color:#222;text-align:center}
.links__label{font-size:7px}
.links__value{font-size:8px;font-weight:700;display:flex;align-items:center;gap:2px}
svg{flex:none}
</style>
</head>
<body>

<section class="card card--front">
  <div class="accent-bar"></div>
  <div class="brand">
    <span class="brand__dot"></span>
    <span class="brand__name">Harbor Oncology Partners</span>
  </div>
  <div class="contact">
    <div class="contact__label">CONTACT US</div>
    <div class="contact__phone">253.400.7218</div>
  </div>
  <div class="offer">
    <h2 class="offer__title">What we Offer</h2>
    <p>This is Photoshop's version&nbsp; of Lorem Ipsum. Proin gravida nibh vel velit auctor aliquet. Aenean sollicitudin.</p>
    <p>This is Photoshop's version&nbsp; of Lorem Ipsum. Proin gravida nibh vel velit auctor aliquet. Aenean sollicitudin, lorem quis bibendum auctor.</p>
  </div>
  <div class="map" role="img" aria-label="Street map showing the office location"></div>
  <div class="footer-band"></div>
</section>

<section class="card card--back">
  <div class="profile">
    <div class="profile__photo" role="img" aria-label="Headshot of Dr. Marcus Whitfield"></div>
    <div class="profile__name">DR. MARCUS WHITFIELD</div>
    <div class="profile__role">MD PhD, Radiation Oncology</div>
    <div class="about">
      <h2 class="about__title">About Dr. Marcus Whitfield</h2>
      <p>Harbor Oncology Partners has been serving patients in the South Puget Sound Region with offices located in Puyallup, Washington. Our Cancer Treatment Center is made up of highly skilled medical professionals who deeply value your health and wellbeing. We take great pride in providing our community with high quality, patient-centric care and health education.</p>
      <p>Proactive and preventative measures help keep our community healthier, and we work with that idea in mind. Harbor Oncology Partners has the wellness services you'd like when you're feeling fine, and the emergency services you need when illness or injury strikes. Come in for a check-up.</p>
    </div>
  </div>
  <div class="office">
    <div class="office__title">Office Location</div>
    <div class="office__address">
      <svg width="7" height="9" viewBox="0 0 10 14"><path d="M5 0a5 5 0 0 0-5 5c0 3.5 5 9 5 9s5-5.5 5-9a5 5 0 0 0-5-5zm0 7a2 2 0 1 1 0-4 2 2 0 0 1 0 4z" fill="#333"/></svg>
      4175 N. Larchmont, Puyallup, WA 98461
    </div>
  </div>
  <div class="office__rule"></div>
  <div class="links">
    <div>
      <div class="links__label">Call Us</div>
      <div class="links__value">
        <svg width="8" height="8" viewBox="0 0 16 16"><path d="M3.6 1l2.6 3-1.4 1.8c.9 2 2.4 3.5 4.4 4.4L11 8.8l3 2.6-1.4 2.6C7 14 2 9 2 2.4z" fill="#222"/></svg>
        253.400.7218
      </div>
    </div>
    <div>
      <div class="links__label">Website</div>
      <div class="links__value">
        <svg width="8" height="8" viewBox="0 0 16 16"><circle cx="8" cy="8" r="7" fill="none" stroke="#222" stroke-width="2"/><path d="M1 8h14M8 1c3 3 3 11 0 14M8 1c-3 3-3 11 0 14" fill="none" stroke="#222" stroke-width="1.4"/></svg>
        harboroncologyhub.com
      </div>
    </div>
  </div>
</section>

</body>
</html>
```